Biz technology consulting firm like a global company (better than Corvellant, etc)

Check word document high level requirements, a_design_webpage_content attached providing more details for content and message to convey to potential customers..  Create a crisp, clear and engaging business consulting website design that allows the user to understand the value that Brimquora can deliver to their company.  We focus on innovation, simplification, creative solutions, digital transformations ERP, CRM, Analytics, project management, making IT simple and coaching enterprises how to align and implement technologies to support business strategy and goals. Whether a startup or a global billion dollar firm, we increase EBITDA through innovation and digital transformation.  

I desire to have sections that highlight each of the core areas such as: (**Please see  brimquora.example and the design word document that is attached below for core areas of focus**)

Feel free to go to Brimquora.example and review the basic categories to understand at a very high level the categories that are key.

Help me create a brand and website that engages startups, Private Equity firms seeking carve-out, integration experience and large corporate enterprises searching to convert to data driven and customer focused enterprises.  
Hero section with a tagline that emphasizes the company's focus on Tilting the view.  We help you visualize outcomes with a positive and collaborative solution driven mindset.  When you look at life through a different "positive" lens, you can convert all problems to opportunities.  Align your IT team with your business goals and you quickly realize the value of all processes and technology deployed in your enterprise; increasing EBITDA, morale, and long term success.

We evaluate your current state, create a custom roadmap for alignment, coach  and empower you to lead while removing the uncertainty and silos.  Partner with the experts who help make business and technology simple and effective
Call-to-action section encouraging visitors to learn more about the company's services and expertise
Services -- detail provided in the attached word document (please use)
Section providing an overview of the company's services, including digital transformation, strategy, change management, CRM, ERP, automation, AI, data / analytics, process optimization, carve-outs, integrations, scaling, risk mitigation, security and marketing.
Call-to-action section encouraging visitors to learn more about the company's expertise and how it can help their business and encouraging visitors to schedule a consultation or assessment.
Footer
Navigation menu
Contact information
LinkedIn link
The website should have a modern and professional design, with a focus on clear messaging and easy navigation. The color scheme will be clean and simple, with a mix of colors to convey trust, reliability, and innovation. The website will be optimized for search engines and mobile devices, ensuring that visitors can easily access the site from any device.

Companies who desire to grow their business, optimize their processes, maximize the output of human capital and profitablity.

Business Technology consulting

• designer should choose for professional audience

• easy navigation, engaging flow, professional layout and colors that represent confidence, excellence and innovation in a world full of change.
• I would like to see you blend in the play on PIVOT's (changes that we face in business and life), the different way we may look at things and the unique way we solve problems. All of these are options to Tilt the view and leverage the unique views of individuals, millions of data points, workflow and technology enablers to deliver maximize value to your enterprise

```html
<!DOCTYPE html>
<html lang="en">
<head>
<meta charset="utf-8">
<title>Brimquora — Business Technology Consulting</title>
<link href="https://fonts.googleapis.com/css2?family=Poppins:wght@400;500;600;700&display=swap" rel="stylesheet">
<style>
:root{
  --navy:#1f2a6e;
  --navy-dark:#151d52;
  --blue:#2f6fd6;
  --sky:#eaf1fb;
  --sky-2:#dde8f7;
  --ink:#1b1f2e;
  --muted:#5b6172;
  --line:#d8dfeb;
  --white:#ffffff;
}
*{box-sizing:border-box;margin:0;padding:0}
html,body{width:1200px;height:4004px;overflow:hidden}
body{font-family:"Poppins",sans-serif;color:var(--ink);background:var(--white);position:relative}
.abs{position:absolute}
p{font-size:13px;line-height:1.7;color:var(--muted)}
h2{font-size:26px;font-weight:600;color:var(--ink);line-height:1.3}
.btn{display:inline-block;background:var(--navy);color:var(--white);font-size:12px;font-weight:500;padding:9px 20px;border-radius:20px;text-decoration:none}
.photo{background:linear-gradient(135deg,#b8c7dc,#6f86a8 55%,#2e3b5a)}
.photo.warm{background:linear-gradient(135deg,#e3d6c6,#9aa7b9 50%,#3b4763)}

/* header */
.site-header{left:0;top:0;width:1200px;height:80px;background:var(--sky)}
.brand{left:140px;top:20px}
.brand-name{font-size:26px;font-weight:700;color:var(--navy);letter-spacing:1px;line-height:1}
.brand-tag{font-size:10px;color:var(--blue);margin-top:3px}
.nav{right:140px;top:22px;display:flex;gap:30px;align-items:center;font-size:12px;font-weight:500;color:var(--ink)}

/* hero */
.hero{left:0;top:80px;width:1200px;height:460px;background:var(--sky)}
.hero-title{left:140px;top:150px;font-size:44px;font-weight:700;color:var(--navy);line-height:1.2}
.hero-sub{left:140px;top:215px;width:360px;font-size:17px;font-weight:600;color:var(--navy);line-height:1.5}
.hero-btn{left:140px;top:300px}
.hero-arch{left:740px;top:40px;width:320px;height:420px;border:2px solid var(--navy);border-radius:160px 160px 0 0}
.hero-photo{left:760px;top:40px;width:300px;height:420px;border-radius:150px 150px 0 0}

/* innovative */
.innov-photo{left:140px;top:632px;width:240px;height:200px;border-radius:4px}
.innov-photo2{left:300px;top:760px;width:120px;height:150px;border:4px solid var(--white)}
.innov-text{left:588px;top:668px;width:470px}
.innov-text p{margin:14px 0 18px}

/* benefits */
.benefits-title{left:0;top:1058px;width:1200px;text-align:center}
.benefit{top:1140px;width:200px}
.benefit-icon{width:40px;height:40px;border-radius:8px;background:var(--sky-2);display:flex;align-items:center;justify-content:center}
.benefit h3{font-size:17px;font-weight:600;margin:18px 0 8px}
.benefit p{font-size:11px;line-height:1.6}
.more{display:flex;gap:6px;align-items:center;font-size:12px;font-weight:500;color:var(--navy);margin-top:12px}

/* unleash */
.unleash{left:0;top:1420px;width:1200px;height:420px;background:var(--sky)}
.unleash-text{left:140px;top:46px;width:440px}
.unleash-text p{margin-top:14px;font-size:12px}
.unleash-photo{left:780px;top:40px;width:280px;height:290px;border-radius:140px 140px 0 0}
.unleash-photo2{left:700px;top:240px;width:160px;height:130px;border:4px solid var(--white)}

/* why partner */
.why-title{left:0;top:1935px;width:1200px;text-align:center;font-size:22px}
.why-list{left:140px;top:2024px;width:260px;list-style:none}
.why-list li{font-size:12px;color:var(--ink);padding:7px 0;border-bottom:1px solid var(--line);display:flex;gap:6px}
.why-list li.active{color:var(--blue);font-weight:500}
.why-photo{left:452px;top:2030px;width:268px;height:420px;border-radius:16px}
.why-detail{left:768px;top:2040px;width:292px}
.why-detail h3{font-size:15px;font-weight:600}
.why-detail p{margin-top:22px;font-size:12px}

/* alignment */
.align-photo{left:140px;top:2560px;width:240px;height:300px;border-radius:120px 120px 0 0}
.align-photo2{left:320px;top:2680px;width:200px;height:220px;border:4px solid var(--white);border-radius:8px}
.align-text{left:588px;top:2560px;width:472px}
.align-text p{margin-top:14px;font-size:12px}
.align-text .btn{margin-top:22px}

/* next */
.next-text{left:140px;top:2980px;width:450px}
.next-text p{margin-top:14px;font-size:12px}
.next-arch{left:760px;top:2990px;width:300px;height:340px;border:2px solid var(--navy);border-radius:150px 150px 0 0}
.next-photo{left:780px;top:2980px;width:280px;height:340px;border-radius:140px 140px 0 0}
.next-photo2{left:730px;top:3200px;width:170px;height:150px;border:4px solid var(--white)}

/* connect */
.connect{left:140px;top:3420px;width:920px;height:262px;background:var(--sky-2);border-radius:16px;text-align:center}
.connect h2{color:var(--blue);margin-top:42px;font-size:26px}
.connect p{width:520px;margin:14px auto 0;font-size:12px}
.connect-row{display:flex;justify-content:center;gap:24px;align-items:center;margin-top:26px}
.phone{display:flex;gap:10px;align-items:center;font-size:13px;font-weight:600;color:var(--navy)}
.phone-dot{width:36px;height:36px;border-radius:50%;background:var(--navy);display:flex;align-items:center;justify-content:center}

/* footer */
.footer-brand{left:140px;top:3752px;width:250px}
.footer-brand p{font-size:11px;margin-top:14px}
.footer-col{top:3752px}
.footer-col h4{font-size:13px;font-weight:600;color:var(--navy);margin-bottom:12px}
.footer-col li{list-style:none;font-size:11px;color:var(--muted);line-height:2.1;display:flex;gap:8px;align-items:center}
.footer-bar{left:140px;top:3950px;width:920px;border-top:1px solid var(--line);padding-top:14px;display:flex;justify-content:space-between;font-size:10px;color:var(--muted)}
.socials{display:flex;gap:8px}
.socials span{width:18px;height:18px;border-radius:50%;background:var(--navy);display:block}
</style>
</head>
<body>

<header class="abs site-header">
  <div class="abs brand"><div class="brand-name">BRIMQUORA</div><div class="brand-tag">Business Technology Consulting</div></div>
  <nav class="abs nav">
    <span>Home</span><span>About Us</span><span>Service</span><span>Blog</span>
    <a class="btn" href="#contact">Contact</a>
  </nav>
</header>

<section class="abs hero">
  <h1 class="abs hero-title">Tilting the View</h1>
  <div class="abs hero-sub">Visualizing Outcomes with a Positive and Collaborative Mindset.</div>
  <a class="abs btn hero-btn" href="#">Learn More</a>
  <div class="abs hero-arch"></div>
  <div class="abs photo hero-photo" role="img" aria-label="Smiling consultant in a suit working at a laptop"></div>
</section>

<div class="abs photo innov-photo" role="img" aria-label="Team meeting around a digital display in an office"></div>
<div class="abs photo warm innov-photo2" role="img" aria-label="Business colleagues talking"></div>
<div class="abs innov-text">
  <h2>Innovative Solutions</h2>
  <p>We believe in pushing the boundaries of what is possible. Our team of experts are dedicated to crafting innovative solutions that help your business thrive. From cutting-edge AI and analytics to customer loyalty and digital transformation, we provide what you need to succeed in today's fast-paced business world.</p>
  <a class="btn" href="#">Learn More</a>
</div>

<h2 class="abs benefits-title">Our Benefits</h2>
<div class="abs benefit" style="left:140px">
  <div class="benefit-icon"><svg width="20" height="20" viewBox="0 0 20 20"><circle cx="7" cy="7" r="3" fill="none" stroke="#2f6fd6" stroke-width="1.6"/><circle cx="14" cy="8" r="2.5" fill="none" stroke="#2f6fd6" stroke-width="1.6"/><path d="M2 17 q5 -7 10 0 M11 16 q3 -5 7 0" fill="none" stroke="#2f6fd6" stroke-width="1.6"/></svg></div>
  <h3>People</h3>
  <p>Empowering the workforce, leadership, and collaboration.</p>
  <div class="more">Learn More <span>→</span></div>
</div>
<div class="abs benefit" style="left:380px">
  <div class="benefit-icon"><svg width="20" height="20" viewBox="0 0 20 20"><rect x="2" y="3" width="6" height="6" fill="none" stroke="#2f6fd6" stroke-width="1.6"/><rect x="12" y="11" width="6" height="6" fill="none" stroke="#2f6fd6" stroke-width="1.6"/><path d="M8 6 h7 v5" fill="none" stroke="#2f6fd6" stroke-width="1.6"/></svg></div>
  <h3>Process</h3>
  <p>Visualizing the flow of work, efficiency, and optimization.</p>
  <div class="more">Learn More <span>→</span></div>
</div>
<div class="abs benefit" style="left:620px">
  <div class="benefit-icon"><svg width="20" height="20" viewBox="0 0 20 20"><rect x="2" y="3" width="16" height="11" rx="1" fill="none" stroke="#2f6fd6" stroke-width="1.6"/><path d="M7 17 h6" stroke="#2f6fd6" stroke-width="1.6"/></svg></div>
  <h3>Systems</h3>
  <p>Depicting technology, integration, and interconnectedness.</p>
  <div class="more">Learn More <span>→</span></div>
</div>
<div class="abs benefit" style="left:860px">
  <div class="benefit-icon"><svg width="20" height="20" viewBox="0 0 20 20"><circle cx="10" cy="10" r="7" fill="none" stroke="#2f6fd6" stroke-width="1.6"/><circle cx="10" cy="10" r="3" fill="none" stroke="#2f6fd6" stroke-width="1.6"/></svg></div>
  <h3>Alignment</h3>
  <p>This can be represented by elements coming together.</p>
  <div class="more">Learn More <span>→</span></div>
</div>

<section class="abs unleash">
  <div class="abs unleash-text">
    <h2>Unleash Your Potential</h2>
    <p>The agency can help establish alignment and accountability within the organization, ensuring that all initiatives are aligned with business goals and promoting a culture of active solutioning. By addressing potential resource challenges and risks, the agency can assist in optimizing resource allocation and planning for future growth.</p>
    <p>The agency can help the organization focus on what adds value to the business, with a strong emphasis on customer needs and wants, ultimately driving customer satisfaction and loyalty.</p>
  </div>
  <div class="abs photo unleash-photo" role="img" aria-label="Two business people reviewing documents"></div>
  <div class="abs photo unleash-photo2" role="img" aria-label="Digital technology network graphic"></div>
</section>

<h2 class="abs why-title">WHY Partner With BRIMQUORA</h2>
<ul class="abs why-list">
  <li class="active"><span>01</span>Enhanced IT Roadmap Visibility</li>
  <li><span>02</span>Improved Written Communication</li>
  <li><span>03</span>Cross-Functional Awareness and Collaboration</li>
  <li><span>04</span>Proactive Problem Solving</li>
  <li><span>05</span>Mentoring and Coaching</li>
  <li><span>06</span>Business Continuity and Risk Mitigation</li>
  <li><span>07</span>Innovation and Collaboration Tools</li>
  <li><span>08</span>Alignment and Accountability</li>
  <li><span>09</span>Resource Optimization and Planning</li>
  <li><span>10</span>Customer-Centric Approach</li>
</ul>
<div class="abs photo warm why-photo" role="img" aria-label="Colleagues shaking hands in a bright office"></div>
<div class="abs why-detail">
  <h3>Enhanced IT Roadmap Visibility</h3>
  <p>A digital transformation agency can improve IT roadmap visibility and awareness throughout the organization, ensuring that technology initiatives are aligned with business objectives and promoting collaboration among IT team members and other departments.</p>
</div>

<div class="abs photo align-photo" role="img" aria-label="Team discussing plans around a table"></div>
<div class="abs photo warm align-photo2" role="img" aria-label="Consultants in a meeting"></div>
<div class="abs align-text">
  <h2>When Was Your Last Alignment?</h2>
  <p>Engaging in critical conversations with key IT and operations leaders to understand the current state of processes and identify areas for improvement that align with business goals. Assessing the level of completeness, accuracy, and data stamp of IT documentation to ensure that improvements are aligned with business objectives and promote business continuity.</p>
  <p>Improving IT roadmap visibility and awareness throughout the organization to ensure that identified areas for improvement are aligned with critical business initiatives and strategic objectives.</p>
  <a class="btn" href="#">Learn More</a>
</div>

<div class="abs next-text">
  <h2>Where Does Your Business Desire To Go Next?</h2>
  <p>Our strategic consulting services are tailored to align your business objectives with actionable technology initiatives, enabling you to navigate challenges, seize opportunities and achieve your business goals with confidence. We specialize in optimizing processes to enhance efficiency, reduce costs, and drive operational excellence, ensuring that your business operates at its full potential.</p>
  <p>Elevate your customer engagement and loyalty with our CRM solutions, designed to deliver exceptional customer experiences and foster lasting relationships.</p>
</div>
<div class="abs next-arch"></div>
<div class="abs photo next-photo" role="img" aria-label="Business team gathered around a laptop"></div>
<div class="abs photo warm next-photo2" role="img" aria-label="Consultant working at a desk"></div>

<section class="abs connect" id="contact">
  <h2>Let's Connect</h2>
  <p>Get in touch with our representatives and start your journey on expanding your company and making your business better, more agile and profitable.</p>
  <div class="connect-row">
    <div class="phone"><span class="phone-dot"><svg width="16" height="16" viewBox="0 0 16 16"><path d="M4 2 l2 3 -1.5 1.5 q1.5 3 4 4 l1.5 -1.5 3 2 -1 2.5 q-6 0 -9 -8z" fill="#fff"/></svg></span>123 456 7890</div>
    <a class="btn" href="#">Get In Touch</a>
  </div>
</section>

<div class="abs footer-brand">
  <div class="brand-name">BRIMQUORA</div><div class="brand-tag">Business Technology Consulting</div>
  <p>Working closely with you to understand your goals and create tailored solutions that work for you.</p>
</div>
<div class="abs footer-col" style="left:460px"><h4>Quick Links</h4><ul><li>Home</li><li>About Us</li><li>Service</li><li>Blog</li></ul></div>
<div class="abs footer-col" style="left:640px"><h4>Site Policy</h4><ul><li>Privacy Policy</li><li>Terms &amp; Condition</li><li>Disclaimer</li></ul></div>
<div class="abs footer-col" style="left:850px"><h4>Contact Info</h4><ul>
  <li><svg width="10" height="12" viewBox="0 0 10 12"><path d="M5 0 a4 4 0 0 1 4 4 c0 3 -4 8 -4 8 s-4 -5 -4 -8 a4 4 0 0 1 4 -4z" fill="#1f2a6e"/></svg>Address Line 1, Address Line 2</li>
  <li><svg width="12" height="10" viewBox="0 0 12 10"><rect width="12" height="10" rx="1" fill="#1f2a6e"/></svg>info@brimquora.example</li>
  <li><svg width="10" height="10" viewBox="0 0 16 16"><path d="M4 2 l2 3 -1.5 1.5 q1.5 3 4 4 l1.5 -1.5 3 2 -1 2.5 q-6 0 -9 -8z" fill="#1f2a6e"/></svg>123 456 7890</li>
</ul></div>
<div class="abs footer-bar"><span>© 2023 Brimquora. All Right Reserved</span><div class="socials"><span></span><span></span><span></span><span></span></div></div>

</body>
</html>
```